Wedding Startup Full Website Design

We've just completed our online platform and need to create a website that represents our brand and vision, and clearly communicates our features and value proposition to potential users. There are a minimum of 4 pages that need to be designed. One geared toward wedding professionals (venues/vendors/coordinators), another toward engaged couples, one showcasing features, and an 'About Us' page.

The designer will creative freedom to create a unique UI/UX as long as it represents our brand and is relevant to our target audience/market. The ideal candidate will be able to assume the mindset of someone working in the wedding industry and/or an engaged couple. Ability to create illustrations is a plus.

Copy will be provided as needed. We will reimburse for stock images (pending approval before purchasing), but sourcing the stock images will be the responsibility of the designer.

Our current website: https://www.trelmora.com
Updates

Our project has now been guaranteed! We look forward to finding the perfect design for our site pages!

Still waiting for a design that stands out from the rest and aligns with the creative brief.

Target Market(s)

Wedding Professionals and Engaged Couples

Industry/Entity Type

Wedding

Number of Pages Required

4 page

Font styles to use
Sans Serif

Colors
ffffff
fbd4d5
f59195
33a6d7
cadf82
86cfc6

Requirements
Must have
• Common sense stuff like having a unified brand that accurately represents our platform, speaks to our target market, and clearly articulates our vision
Nice to have
• Illustrations
Should not have
• Overly cheesy or childish. We want to be professional but still embrace the wedding culture.

```html
<!DOCTYPE html>
<html lang="en">
<head>
<meta charset="utf-8">
<title>Trelmora — Smarter Wed Planning</title>
<link href="https://fonts.googleapis.com/css2?family=Bree+Serif&display=swap" rel="stylesheet">
<style>
:root{
  --teal:#139a8c;
  --teal-bright:#17a596;
  --ink:#111111;
  --muted:#9a9a9a;
  --white:#ffffff;
  --logo:#6cb0df;
  --bar:#000000;
}
*{margin:0;padding:0;box-sizing:border-box}
html,body{width:1040px;height:1200px;overflow:hidden;background:var(--white)}
body{position:relative;font-family:"Bree Serif",Georgia,serif;color:var(--ink)}
.abs{position:absolute}

/* hero */
.hero-photo{left:0;top:0;width:1040px;height:484px;
  background:linear-gradient(100deg,#6b5a45 0%,#a48d6f 22%,#7f8a6a 40%,#3f4a3a 60%,#2a2a33 78%,#3b2f3a 100%)}
.site-header{left:0;top:0;width:1040px;height:88px;background:rgba(20,24,22,.62)}
.brand{left:64px;top:14px;font-size:46px;color:var(--logo);line-height:1}
.nav a{position:absolute;top:30px;font-size:19px;text-decoration:none;color:var(--white)}
.nav .active{color:var(--teal-bright)}
.btn-outline{border:2px solid var(--teal);color:var(--teal-bright);font-size:19px;
  display:flex;align-items:center;justify-content:center;letter-spacing:.5px}
.header-demo{left:808px;top:20px;width:160px;height:44px}
.welcome{left:380px;top:132px;width:280px;height:280px;border-radius:50%;
  background:rgba(220,220,220,.82);border:5px solid var(--white);
  box-shadow:0 0 0 8px rgba(255,255,255,.25),0 0 18px rgba(0,0,0,.35);text-align:center}
.welcome svg{position:absolute;left:112px;top:44px}
.welcome .tag{position:absolute;top:112px;width:100%;font-size:16px;color:var(--ink)}
.welcome h1{position:absolute;top:142px;width:100%;font-size:23px;font-weight:400;color:var(--teal)}
.welcome .start{position:absolute;left:81px;top:184px;width:118px;height:32px;
  border:2px solid var(--ink);border-radius:3px;font-size:14px;line-height:28px}

/* steps */
.steps-title{left:0;top:494px;width:1020px;text-align:center;font-size:23px;color:var(--teal)}
.steps-rule{left:142px;top:538px;width:756px;height:2px;background:var(--teal)}
.steps-heart{left:500px;top:526px}
.step-label{left:64px;font-size:18px;display:flex;align-items:center;gap:6px}
.step-label::before{content:"";width:9px;height:9px;border-radius:50%;background:var(--teal)}
.step-line{left:245px;top:614px;width:2px;height:162px;background:var(--teal)}
.step-num{width:37px;height:37px;border-radius:50%;border:2px solid var(--teal);background:var(--white);
  font-size:12px;display:flex;align-items:center;justify-content:center;left:228px}
.step-num.filled{background:var(--teal);color:var(--white)}
.step-text{left:298px;width:340px;font-size:15px;line-height:20px;color:var(--muted)}
.step-text.current{color:var(--ink)}
.step-text a{color:var(--teal);text-decoration:none}
.app-preview{left:662px;top:560px;width:314px;height:242px;border-radius:8px;
  background:linear-gradient(180deg,#f4f4f4,#e6e8ea);border:1px solid #cfcfcf}

/* features */
.feature-photo{left:0;top:822px;width:1040px;height:272px;
  background:linear-gradient(100deg,#4a3e30 0%,#5d5040 30%,#3a3e33 55%,#2b2a2e 75%,#3a2f36 100%)}
.feature{width:250px;text-align:center}
.feature svg{display:block;margin:0 auto}
.feature h2{font-size:17px;font-weight:400;color:var(--teal-bright);margin-top:6px}
.feature p{font-size:15px;line-height:22.5px;color:var(--white);margin-top:2px}

/* call to action */
.cta-bar{left:0;top:1109px;width:1040px;height:91px;background:var(--bar)}
.cta-title{left:54px;top:1140px;font-size:23px;color:var(--teal)}
.cta-text{left:284px;top:1119px;width:520px;text-align:center;font-size:15px;line-height:24px;color:var(--white)}
.cta-demo{left:822px;top:1138px;width:164px;height:45px;border-radius:3px}
</style>
</head>
<body>

<div class="abs hero-photo" role="img" aria-label="Photo of a woman in a floral dress setting a lantern on a table beside wooden chairs and white hydrangeas"></div>

<header class="abs site-header">
  <div class="abs brand">Trelmora</div>
  <nav class="nav">
    <a class="active" style="left:350px" href="#">ABOUT US</a>
    <a style="left:465px" href="#">FEAYURES</a>
    <a style="left:577px" href="#">FOR COUPLES</a>
  </nav>
  <a class="abs btn-outline header-demo">ACCESS&nbsp;&nbsp;DEMO</a>
</header>

<section class="abs welcome">
  <svg width="50" height="46" viewBox="0 0 50 46"><path d="M25 44 C8 30 2 22 2 13 C2 6 7 2 13 2 C18 2 22 5 25 9 C28 5 32 2 37 2 C43 2 48 6 48 13 C48 22 42 30 25 44Z" fill="#139a8c"/></svg>
  <div class="tag">Smarter Wed Planning™</div>
  <h1>WELCOME TO TRELMORA</h1>
  <div class="start">GET STARTED</div>
</section>

<h2 class="abs steps-title" style="font-weight:400">HOW TO GET STARTED</h2>
<div class="abs steps-rule"></div>
<svg class="abs steps-heart" width="36" height="32" viewBox="0 0 36 32"><path d="M18 31 C6 21 1 15 1 9 C1 4 5 1 9.5 1 C13 1 16 3 18 6 C20 3 23 1 26.5 1 C31 1 35 4 35 9 C35 15 30 21 18 31Z" fill="#139a8c"/></svg>

<div class="abs step-label" style="top:586px">SIGN UP</div>
<div class="abs step-label" style="top:675px">COLLABORATE</div>
<div class="abs step-label" style="top:761px">CONNECT</div>

<div class="abs step-line"></div>
<div class="abs step-num filled" style="top:578px">1</div>
<div class="abs step-num" style="top:667px">2</div>
<div class="abs step-num" style="top:756px">3</div>

<p class="abs step-text current" style="top:574px">Create a free account on Trelmora to access popular collaboration tools.&nbsp; <a href="#">Get Started</a></p>
<p class="abs step-text" style="top:656px">Add clients within the application to better organize and manage event details.</p>
<p class="abs step-text" style="top:751px">Linking your bank account within Trelmora to allow for seamless payments and monitoring.</p>

<div class="abs app-preview" role="img" aria-label="Tablet showing the planning dashboard with a client profile and ceremony guideline form"></div>

<div class="abs feature-photo" role="img" aria-label="Dimmed photo of the lantern table setting with wooden chairs"></div>

<div class="abs feature" style="left:83px;top:840px">
  <svg width="94" height="94" viewBox="0 0 94 94"><rect x="20" y="20" width="54" height="54" transform="rotate(45 47 47)" fill="none" stroke="#17a596" stroke-width="2"/><path d="M36 55 h24 a7 7 0 0 0 0-14 a10 10 0 0 0-19-2 a8 8 0 0 0-5 16Z M47 58 v-12 M42 50 l5-5 5 5" fill="none" stroke="#17a596" stroke-width="1.6"/></svg>
  <h2>REALTIME COLLABORATION.</h2>
  <p>There are often disconnects in the communication channel. At the core of Trelmora we ensure everyone is updated in real time with event information</p>
</div>
<div class="abs feature" style="left:395px;top:840px">
  <svg width="94" height="94" viewBox="0 0 94 94"><rect x="20" y="20" width="54" height="54" transform="rotate(45 47 47)" fill="#139a8c"/><circle cx="47" cy="46" r="15" fill="none" stroke="#fff" stroke-width="2"/><path d="M41 41h12M41 46h12M41 51h12M55 57l6 5" stroke="#fff" stroke-width="1.8" fill="none"/></svg>
  <h2>CLOUD STORAGE.</h2>
  <p>No longer do you have to remember where every piece of information is saved. With Trelmora all your information is available in one central location.</p>
</div>
<div class="abs feature" style="left:707px;top:840px">
  <svg width="94" height="94" viewBox="0 0 94 94"><rect x="20" y="20" width="54" height="54" transform="rotate(45 47 47)" fill="none" stroke="#17a596" stroke-width="2"/><path d="M37 56 h20 l-3-4 v-9 a7 7 0 0 0-14 0 v9Z M44 59 a3 3 0 0 0 6 0" fill="none" stroke="#17a596" stroke-width="1.6"/></svg>
  <h2>NOTIFICATIONS &amp; DEADLINES.</h2>
  <p>Every detail is important and matters. Trelmora helps make sure that all the information for an event are inputted and updated in a timely manner.</p>
</div>

<footer>
  <div class="abs cta-bar"></div>
  <div class="abs cta-title">GET STARTED TODAY</div>
  <p class="abs cta-text">We recently launched a demo version of Trelmora to allow users to see and interact with our platform. Create a free account and see how Trelmora is changing the wedding planning process!</p>
  <a class="abs btn-outline cta-demo">ACCESS&nbsp;&nbsp;DEMO</a>
</footer>

</body>
</html>
```